Wildlife photographer Website

The website is to be a "resume" of pictures and awards won by Nora. Lean heavy to outdoor wildlife.
She will post articles and have ability to interact with fans.

I will add some of her pictures tonight,

Target Market(s)

Terra Quarterly .....anyone looking to hire a wildlife photographer.

Industry/Entity Type

Professional Photography

Contact Information for Business Card

Nora Falkett
4817 Maple Hollow Lane
Columbia MD 21078
443-581-2094
Nora@FernOwlPix.com

Coding

Coded - Design and coding required

Number of Pages Required

5+ page

Requirements
Must have
• New Logo
Nice to have
• Nature, and eye catching graphics

```html
<!DOCTYPE html>
<html lang="en">
<head>
<meta charset="utf-8">
<title>Nora Falkett – Wildlife Photographer</title>
<link rel="stylesheet" href="https://fonts.googleapis.com/css2?family=Poppins:wght@300;400&family=Mulish:wght@400;500&family=Roboto+Condensed:wght@400&display=swap">
<style>
:root{
  --yellow:#fcd42b;
  --ink:#1d1d1d;
  --text:#2a2a2a;
  --panel:rgba(72,73,80,.9);
  --white:#ffffff;
  --rule:#e4e4e4;
  --footer-text:#f2f2f2;
}
*{margin:0;padding:0;box-sizing:border-box}
html,body{width:1200px;height:3082px;overflow:hidden;background:var(--white)}
body{position:relative;font-family:'Mulish',sans-serif;color:var(--text)}
.abs{position:absolute}
.btn{position:absolute;display:flex;align-items:center;justify-content:center;background:var(--yellow);color:var(--ink);font-family:'Roboto Condensed',sans-serif;font-size:21px;border-radius:3px}

/* header */
.site-header{position:absolute;left:0;top:0;width:1200px;height:100px;background:var(--white)}
.brand-mark{position:absolute;left:160px;top:15px;width:76px;height:76px;border-radius:50%;background:#2f2f33}
.brand-name{position:absolute;left:246px;top:16px;font-family:'Poppins',sans-serif;font-weight:400;font-size:38px;line-height:42px;color:var(--ink)}
.brand-sub{position:absolute;left:248px;top:57px;font-family:'Poppins',sans-serif;font-weight:400;font-size:19px;color:var(--ink)}
.main-nav a{position:absolute;top:42px;font-family:'Roboto Condensed',sans-serif;font-size:19px;color:var(--ink);text-decoration:none}

/* hero */
.hero-photo{position:absolute;left:0;top:100px;width:1200px;height:504px;background:linear-gradient(180deg,#c9d3e6 0%,#e8edf5 45%,#f4f6fa 75%,#dfe4ee 100%)}
.hero-card{position:absolute;left:161px;top:222px;width:413px;height:261px;background:var(--panel);border-left:7px solid var(--yellow);color:var(--white)}
.hero-card .welcome{position:absolute;left:36px;top:48px;font-size:23px}
.hero-card .title{position:absolute;left:36px;top:80px;font-size:38px;font-weight:400;white-space:nowrap}
.hero-card .by{position:absolute;left:34px;top:126px;font-size:23px}

/* about */
.about-photo{position:absolute;left:0;top:604px;width:1200px;height:466px;background:linear-gradient(90deg,#efe0cc 0%,#f3e6d6 40%,#ece4d2 70%,#efe3d4 100%)}
.portrait{position:absolute;left:168px;top:680px;width:328px;height:314px;border-radius:50%;border:2px solid var(--yellow)}
.portrait-fill{position:absolute;left:174px;top:688px;width:316px;height:300px;border-radius:50%;background:linear-gradient(180deg,#3e5a4a 0%,#5d7784 45%,#8b6a4e 75%,#6b5a4b 100%)}
.about-title{position:absolute;left:522px;top:700px;font-family:'Mulish',sans-serif;font-size:27px;color:var(--ink)}
.about-text{position:absolute;left:524px;top:744px;width:520px;font-size:13.6px;line-height:24.4px;color:var(--ink)}

/* featured */
.section-title{position:absolute;left:0;width:1200px;text-align:center;font-family:'Poppins',sans-serif;font-weight:400;color:var(--ink)}
.section-lead{position:absolute;left:200px;top:1198px;width:800px;text-align:center;font-size:13.6px;line-height:24.4px;color:var(--ink)}
.tile{position:absolute}

/* articles */
.article{position:absolute;left:161px;width:401px;height:74px}
.article .date{position:absolute;left:0;top:0;font-size:15px;color:var(--ink)}
.article .excerpt{position:absolute;left:0;top:28px;font-size:13.4px;color:var(--ink)}
.article .go{position:absolute;left:381px;top:21px}
.article.ruled{border-bottom:2px solid var(--rule)}
.article-photo{position:absolute;left:612px;top:2157px;width:424px;height:329px;background:linear-gradient(180deg,#f2cc8c 0%,#e9c38c 15%,#7d8c94 30%,#55707c 55%,#8d7b5a 70%,#47606a 100%)}

/* footer */
.site-footer{position:absolute;left:0;top:2575px;width:1200px;height:507px;background:linear-gradient(120deg,#2b2a22 0%,#3c3a2a 30%,#24261e 60%,#332f26 100%);color:var(--footer-text)}
.fox-photo{position:absolute;left:0;top:0;width:560px;height:507px;background:radial-gradient(ellipse at 45% 60%,#a35a2e 0%,#6e4025 40%,rgba(50,45,32,0) 75%)}
.footer-mark{position:absolute;left:572px;top:67px;width:76px;height:76px;border-radius:50%;background:var(--white)}
.footer-name{position:absolute;left:658px;top:66px;font-family:'Poppins',sans-serif;font-size:38px;line-height:42px;color:var(--white)}
.footer-sub{position:absolute;left:660px;top:108px;font-family:'Poppins',sans-serif;font-size:19px;color:var(--white)}
.footer-nav a{position:absolute;top:168px;font-size:15px;color:var(--footer-text);text-decoration:none}
.contact-icon{position:absolute;left:571px;width:42px;height:42px;border-radius:50%;background:var(--yellow);display:flex;align-items:center;justify-content:center}
.contact-text{position:absolute;left:624px;font-size:13px;line-height:17px;color:var(--footer-text)}
.social{position:absolute;top:2989px;width:28px;height:28px;border-radius:50%;background:var(--yellow)}
.copyright{position:absolute;left:571px;top:3036px;font-size:11.5px;color:var(--footer-text)}
</style>
</head>
<body>

<header class="site-header">
  <div class="brand-mark"></div>
  <div class="brand-name">Nora Falkett</div>
  <div class="brand-sub">Wildlife Photographer</div>
  <nav class="main-nav">
    <a style="left:621px">About Me</a>
    <a style="left:730px">My Gallery</a>
    <a style="left:843px">Articles</a>
  </nav>
  <div class="btn" style="left:915px;top:32px;width:124px;height:44px">Hire Me</div>
</header>

<section>
  <div class="hero-photo" role="img" aria-label="Female cardinal standing in fresh snow"></div>
  <div class="hero-card">
    <div class="welcome">Welcome to</div>
    <div class="title">Wildlife Photography</div>
    <div class="by">By Nora Falkett</div>
    <div class="btn" style="left:30px;top:167px;width:124px;height:43px">Hire Me</div>
  </div>
</section>

<section>
  <div class="about-photo" role="img" aria-label="Faded photo of the photographer lying on sand with a camera"></div>
  <div class="portrait-fill" role="img" aria-label="Portrait of Nora Falkett by a river with pine trees"></div>
  <div class="portrait"></div>
  <h2 class="about-title" style="font-weight:400">About Nora Falkett</h2>
  <p class="about-text">Lorem ipsum dolor sit amet, consectetuer adipiscing elit, sed diam nonummy nibh euismod tincidunt ut laoreet dlore magna aliquam erat volutpat. Ut wisifd fenim ad minim veniam, quis nostrud exerci tation ullamcorper suscipit lobortis nisl ut aliquip ex ea commodo consequat duis. Lorem ipsum dolor sit amet, consectetuer adipiscing elit, sed diam nonummy nibh euismod tincidunt ut laoreet dlore magna aliquam erat volutpat. Ut wisifd fenim ad minim veniam, quis nostrud exerci tation ullamcorper suscipit lobortis nisl ut aliquip.</p>
  <div class="btn" style="left:526px;top:923px;width:188px;height:44px;font-size:19px">Read More About Me</div>
</section>

<section>
  <h2 class="section-title" style="top:1148px;font-size:33px">Featured Photography Projects</h2>
  <p class="section-lead">Lorem ipsum dolor sit amet, consectetuer adipiscing elit, sed diam nonummy nibh euismod tincidunt ut laoreet dolore magna aliquam erat volutpat. Ut wisi enim ad minim veniam.</p>
  <div class="tile" style="left:161px;top:1264px;width:289px;height:285px;background:linear-gradient(160deg,#e6ecf6,#d9c39a 60%,#eef1f6)" role="img" aria-label="Female cardinal in snow"></div>
  <div class="tile" style="left:161px;top:1554px;width:289px;height:387px;background:linear-gradient(180deg,#2b4a6e,#1e3a5c 50%,#3a4d62)" role="img" aria-label="Harlequin duck swimming in dark water"></div>
  <div class="tile" style="left:456px;top:1264px;width:288px;height:389px;background:linear-gradient(160deg,#cdc2b2,#8c8470 50%,#4f5340)" role="img" aria-label="Hummingbird hovering by a small waterfall"></div>
  <div class="tile" style="left:456px;top:1658px;width:288px;height:283px;background:linear-gradient(180deg,#2a3c60,#a38a6a 50%,#d8dfe9)" role="img" aria-label="Rabbit leaping across snow"></div>
  <div class="tile" style="left:750px;top:1264px;width:288px;height:284px;background:linear-gradient(160deg,#2e3524,#8a5a32 50%,#3d4a2a)" role="img" aria-label="Red fox sitting among bamboo"></div>
  <div class="tile" style="left:750px;top:1553px;width:288px;height:388px;background:linear-gradient(180deg,#8fb0d6,#3d5a38 40%,#b98466 75%,#a07a62)" role="img" aria-label="Photographer hiking on a rocky trail in a pine valley"></div>
  <div class="btn" style="left:533px;top:1971px;width:124px;height:44px">View All</div>
</section>

<section>
  <h2 class="section-title" style="top:2090px;font-size:28px;font-family:'Mulish',sans-serif">Recent Articles</h2>

  <div class="article ruled" style="top:2153px"><div class="date">Mar, 03 2021</div><div class="excerpt">Lorem ipsum dolor sit amet, consectetuer adipiscing sed</div>
    <svg class="go" width="16" height="16" viewBox="0 0 16 16"><circle cx="8" cy="8" r="7" fill="none" stroke="#fcd42b" stroke-width="1.3"/><path d="M7 5l3 3-3 3" fill="none" stroke="#fcd42b" stroke-width="1.3"/></svg></div>
  <div class="article ruled" style="top:2227px"><div class="date">Mar, 05 2021</div><div class="excerpt">Lorem ipsum dolor sit amet, consectetuer adipiscing sed</div>
    <svg class="go" width="16" height="16" viewBox="0 0 16 16"><circle cx="8" cy="8" r="7" fill="none" stroke="#fcd42b" stroke-width="1.3"/><path d="M7 5l3 3-3 3" fill="none" stroke="#fcd42b" stroke-width="1.3"/></svg></div>
  <div class="article ruled" style="top:2301px"><div class="date">Mar, 08 2021</div><div class="excerpt">Lorem ipsum dolor sit amet, consectetuer adipiscing sed</div>
    <svg class="go" width="16" height="16" viewBox="0 0 16 16"><circle cx="8" cy="8" r="7" fill="none" stroke="#fcd42b" stroke-width="1.3"/><path d="M7 5l3 3-3 3" fill="none" stroke="#fcd42b" stroke-width="1.3"/></svg></div>
  <div class="article" style="top:2374px"><div class="date">Mar, 08 2021</div><div class="excerpt">Lorem ipsum dolor sit amet, consectetuer adipiscing sed</div>
    <svg class="go" width="16" height="16" viewBox="0 0 16 16"><circle cx="8" cy="8" r="7" fill="none" stroke="#fcd42b" stroke-width="1.3"/><path d="M7 5l3 3-3 3" fill="none" stroke="#fcd42b" stroke-width="1.3"/></svg></div>

  <div class="btn" style="left:159px;top:2443px;width:105px;height:43px;font-size:19px">View More</div>
  <div class="article-photo" role="img" aria-label="Waves curling on a shoreline at golden hour"></div>
</section>

<footer class="site-footer">
  <div class="fox-photo" role="img" aria-label="Red fox in dark bamboo thicket"></div>
  <div class="footer-mark"></div>
  <div class="footer-name">Nora Falkett</div>
  <div class="footer-sub">Wildlife Photographer</div>
  <nav class="footer-nav">
    <a style="left:571px">Home</a>
    <a style="left:654px">About Me</a>
    <a style="left:763px">My Gallery</a>
    <a style="left:880px">Articles</a>
    <a style="left:975px">Hire Me</a>
  </nav>

  <div class="contact-icon" style="top:211px"><svg width="18" height="18" viewBox="0 0 18 18"><path d="M9 16s-5-5.5-5-9a5 5 0 0110 0c0 3.5-5 9-5 9z" fill="none" stroke="#333" stroke-width="1.2"/><circle cx="9" cy="7" r="1.8" fill="none" stroke="#333" stroke-width="1.2"/></svg></div>
  <div class="contact-text" style="top:220px">4817 Maple Hollow Lane<br>Columbia MD 21078</div>

  <div class="contact-icon" style="top:271px"><svg width="18" height="18" viewBox="0 0 18 18"><path d="M4 2l3 0 1 4-2 1.3a9 9 0 004.7 4.7L12 10l4 1v3a2 2 0 01-2 2A12 12 0 012 4a2 2 0 012-2z" fill="none" stroke="#333" stroke-width="1.2"/></svg></div>
  <div class="contact-text" style="top:284px">443-581-2094</div>

  <div class="contact-icon" style="top:330px"><svg width="18" height="18" viewBox="0 0 18 18"><rect x="2" y="5" width="14" height="10" fill="none" stroke="#333" stroke-width="1.2"/><path d="M2 5l7 6 7-6" fill="none" stroke="#333" stroke-width="1.2"/></svg></div>
  <div class="contact-text" style="top:343px">Nora@FernOwlPix.com</div>

  <div class="copyright" style="top:461px">Copyright © 2021 Nora Falkett Wildlife Photographer. All Rights Reserved.</div>
</footer>

<div class="social" style="left:573px"></div>
<div class="social" style="left:609px"></div>
<div class="social" style="left:645px"></div>
<div class="social" style="left:681px"></div>

</body>
</html>
```